Designing a brochures for an educational counseling service provider

We would like a 4 sided design on a 11x8.5 paper, half folded. I have including a sample design we did to give you an idea of what we envision but we welcome creativity to make beautiful looking flyers. Text for the flier is included as well as our logo.
- The most important thing is capturing our audience/market. We will be handing these flies to schools, organizations and individual clients.

www.plorvaeducationalconsultants.example

Target Market(s)

We are targeting international students wanting to study in the U.S and Canada.

Industry/Entity Type

Education

Requirements
Must have
• - Clean and clear
• - Our logo should visible and well placed.
• - Could you the pictures of students, libraries and school buildings or you could use the pictures we already have.
Nice to have
• We would like this to match business cards.

```html
<!DOCTYPE html>
<html lang="en">
<head>
<meta charset="utf-8">
<title>Plorva International Educational Consultants – Brochure Cover</title>
<link rel="stylesheet" href="https://fonts.googleapis.com/css2?family=Roboto:wght@400;500;700&family=Roboto+Condensed:wght@700&display=swap">
<style>
  :root {
    --backdrop: #e4e5e7;
    --paper: #f4f4f2;
    --navy: #1f4456;
    --navy-deep: #163545;
    --orange: #e8701f;
    --charcoal: #3a3b3d;
    --ink: #2b2b2b;
    --grey-text: #5e6062;
    --white: #ffffff;
  }
  * { box-sizing: border-box; margin: 0; padding: 0; }
  html, body {
    width: 1200px; height: 800px; overflow: hidden;
    background: var(--backdrop);
    font-family: "Roboto", Arial, sans-serif;
  }
  .spread {
    position: absolute; left: 147px; top: 50px;
    width: 906px; height: 700px;
    display: flex;
    box-shadow: 0 10px 30px rgba(0,0,0,.18);
  }
  .panel {
    position: relative; width: 453px; height: 700px;
    background: var(--paper); overflow: hidden;
  }
  .panel--back { border-right: 1px solid #dcdcda; }
  .panel svg.art { position: absolute; inset: 0; width: 453px; height: 700px; }

  /* Back cover: contact block */
  .contact { position: absolute; left: 40px; top: 300px; width: 300px; }
  .contact__title {
    font-family: "Roboto Condensed", Arial, sans-serif;
    color: var(--orange); font-size: 19px; font-weight: 700;
    letter-spacing: .5px; margin-bottom: 8px;
  }
  .contact__line { color: var(--ink); font-size: 11.5px; line-height: 1.5; }

  /* Front cover: brand */
  .brand { position: absolute; left: 190px; top: 120px; display: flex; align-items: center; gap: 10px; }
  .brand__mark { width: 34px; height: 34px; border-radius: 50%; background: var(--navy); }
  .brand__name {
    font-family: "Roboto", Arial, sans-serif; font-weight: 700;
    font-size: 30px; color: var(--navy); letter-spacing: 1px; line-height: 1;
  }
  .brand__sub {
    position: absolute; left: 234px; top: 158px; width: 200px;
    font-size: 8.5px; font-weight: 500; color: var(--navy);
    letter-spacing: 1.4px; text-transform: uppercase; line-height: 1.4;
  }

  .headline {
    position: absolute; left: 182px; top: 405px; width: 265px;
    font-family: "Roboto Condensed", Arial, sans-serif; font-weight: 700;
    color: var(--white); font-size: 12.5px; line-height: 1.3;
    text-transform: uppercase; letter-spacing: .3px;
  }

  .services { position: absolute; left: 30px; top: 478px; list-style: none; }
  .services__item {
    display: flex; align-items: center; height: 36px;
  }
  .services__icon { width: 26px; height: 26px; margin-right: 22px; }
  .services__label {
    font-family: "Roboto Condensed", Arial, sans-serif; font-weight: 700;
    font-size: 15px; color: var(--grey-text); text-transform: uppercase;
    letter-spacing: .3px;
  }
  .services__divider {
    position: absolute; left: 66px; top: 480px; width: 1.5px; height: 140px;
    background: #b9bbbd;
  }

  .footer-strip {
    position: absolute; left: 22px; top: 654px; width: 318px; height: 20px;
    background: var(--navy); color: var(--white);
    font-size: 7.6px; display: flex; align-items: center; justify-content: center;
    gap: 6px; letter-spacing: .2px;
  }
</style>
</head>
<body>
<main class="spread">

  <!-- Back cover -->
  <section class="panel panel--back">
    <svg class="art" viewBox="0 0 453 700" aria-hidden="false">
      <defs>
        <linearGradient id="backPhotoTone" x1="0" y1="0" x2="1" y2="1">
          <stop offset="0" stop-color="#8a5a3c"/>
          <stop offset=".5" stop-color="#5b3a28"/>
          <stop offset="1" stop-color="#c9b9a8"/>
        </linearGradient>
      </defs>
      <polygon role="img" aria-label="Photo of a smiling female student" fill="url(#backPhotoTone)" points="0,0 453,0 453,40 0,200"/>
      <polygon fill="var(--navy)" points="40,222 453,70 453,128 170,232"/>
      <polygon fill="var(--navy)" points="90,268 453,142 453,151 90,277"/>
      <polygon fill="var(--navy)" points="0,570 453,420 453,522 0,650"/>
      <polygon fill="var(--navy-deep)" points="0,668 453,540 453,550 0,678"/>
    </svg>

    <div class="contact">
      <h2 class="contact__title">CONTACT US</h2>
      <p class="contact__line">Executive Director &amp; Independent</p>
      <p class="contact__line">Educational Consultant</p>
      <p class="contact__line">Plorva International Educational Consultants, LLC</p>
      <p class="contact__line">Suite 118b, 4410 Harlow Rd</p>
      <p class="contact__line">Cedarvale, TX 75010</p>
      <p class="contact__line">Phone : 555-013-2480</p>
      <p class="contact__line">Email : nadia@plorvaeducationalconsultants.example</p>
    </div>
  </section>

  <!-- Front cover -->
  <section class="panel panel--front">
    <svg class="art" viewBox="0 0 453 700">
      <defs>
        <linearGradient id="frontPhotoTone" x1="0" y1="0" x2="1" y2="1">
          <stop offset="0" stop-color="#6b4a36"/>
          <stop offset=".55" stop-color="#3e2c22"/>
          <stop offset="1" stop-color="#3f6ea8"/>
        </linearGradient>
      </defs>
      <polygon fill="var(--orange)" points="170,0 262,0 453,100 453,142"/>
      <polygon fill="var(--navy)" points="0,275 453,180 453,214 0,318"/>
      <polygon role="img" aria-label="Photo of a group of smiling international students" fill="url(#frontPhotoTone)" points="170,290 453,222 453,460 170,460"/>
      <rect x="170" y="398" width="283" height="62" fill="var(--charcoal)" opacity=".9"/>
      <polygon fill="var(--orange)" points="362,460 418,460 380,700 324,700"/>
      <polygon fill="var(--orange)" points="428,460 438,460 400,700 390,700"/>
    </svg>

    <div class="brand">
      <span class="brand__mark"></span>
      <span class="brand__name">PLORVA</span>
    </div>
    <p class="brand__sub">International Educational Consultants</p>

    <h1 class="headline">A full-service international educational consulting group serving students and families across the globe.</h1>

    <span class="services__divider"></span>
    <ul class="services">
      <li class="services__item">
        <svg class="services__icon" viewBox="0 0 26 26" fill="none" stroke="#6b6d70" stroke-width="1.6">
          <path d="M3 9 L13 3 L23 9 Z"/><line x1="6" y1="11" x2="6" y2="20"/><line x1="11" y1="11" x2="11" y2="20"/><line x1="15" y1="11" x2="15" y2="20"/><line x1="20" y1="11" x2="20" y2="20"/><line x1="3" y1="22" x2="23" y2="22"/>
        </svg>
        <span class="services__label">Boarding Schools</span>
      </li>
      <li class="services__item">
        <svg class="services__icon" viewBox="0 0 26 26" fill="none" stroke="#6b6d70" stroke-width="1.6">
          <rect x="5" y="3" width="16" height="20" rx="1"/><line x1="9" y1="9" x2="17" y2="9"/><line x1="9" y1="13" x2="17" y2="13"/><line x1="9" y1="17" x2="14" y2="17"/>
        </svg>
        <span class="services__label">College Admission</span>
      </li>
      <li class="services__item">
        <svg class="services__icon" viewBox="0 0 26 26" fill="none" stroke="#6b6d70" stroke-width="1.6">
          <circle cx="9" cy="8" r="3.5"/><circle cx="18" cy="8" r="3.5"/><path d="M3 21 C3 15 15 15 15 21"/><path d="M12 21 C12 15 24 15 24 21"/>
        </svg>
        <span class="services__label">Transfer Students</span>
      </li>
      <li class="services__item">
        <svg class="services__icon" viewBox="0 0 26 26" fill="none" stroke="#6b6d70" stroke-width="1.6">
          <path d="M2 10 L13 5 L24 10 L13 15 Z"/><path d="M7 12.5 V18 C10 20.5 16 20.5 19 18 V12.5"/><line x1="24" y1="10" x2="24" y2="17"/>
        </svg>
        <span class="services__label">Graduate Students</span>
      </li>
    </ul>

    <div class="footer-strip">
      <span>Cedarvale, Texas</span><span>|</span><span>+1-555-013-2480</span><span>|</span><span>info@plorvaeducationalconsultants.example</span>
    </div>
  </section>

</main>
</body>
</html>
```